Can you make a cool and versatile Tarnel Ventures Powerpoint template?
See www.tarnelventures.co.uk and http://www.linkedin.com/company/tarnel-ventures-ltd/ (on the right) to see how the logos are currently used - with interchangeably white and black backgrounds.
Target Market(s)
Marketing managers, product managers in HR technology, HR consultants
Industry/Entity Type
It Company
Font styles to use
Sans Serif
Requirements
Must have
- Master slide design, fonts, color theme, etc. Ideally two variations - one with white background (using colorful logo), one with a darker background (using black/white logo).

```html
<!DOCTYPE html>
<html lang="en">
<head>
<meta charset="utf-8">
<title>Tarnel Ventures – Template with Dark Background V2</title>
<link rel="stylesheet" href="https://fonts.googleapis.com/css2?family=Arimo:wght@400&family=Carlito&display=swap">
<style>
  :root {
    --canvas: #d9d9d9;
    --slide-dark: #222222;
    --slide-dark-soft: #2e2e2e;
    --slide-light: #ffffff;
    --ink: #111111;
    --ink-body: #1a1a1a;
    --on-dark: #ffffff;
    --on-dark-muted: #6a6a6a;
  }
  * { margin: 0; padding: 0; box-sizing: border-box; }
  html, body { width: 1200px; height: 900px; overflow: hidden; }
  body {
    background: var(--canvas);
    position: relative;
    font-family: "Arimo", Arial, sans-serif;
  }
  .sheet-title {
    position: absolute;
    left: 352px; top: 72px;
    font-family: "Carlito", Calibri, sans-serif;
    font-size: 28px;
    font-weight: 400;
    color: var(--ink);
  }
  .slide { position: absolute; overflow: hidden; }
  .slide--dark { background: var(--slide-dark); color: var(--on-dark); }
  .slide--light { background: var(--slide-light); color: var(--ink-body); }
  .backdrop {
    position: absolute; inset: 0;
    background: linear-gradient(135deg, var(--slide-dark-soft) 0%, var(--slide-dark) 70%);
  }
  .brand {
    position: absolute;
    display: flex; align-items: center; gap: 8px;
    color: var(--on-dark);
    white-space: nowrap;
    font-weight: 400;
  }
  .brand--large { font-size: 17px; }
  .brand--medium { font-size: 12px; }
  .brand--tiny { font-size: 5px; }
  .slide__heading {
    position: absolute;
    font-size: 12px;
    color: var(--on-dark);
  }
  .slide__date {
    position: absolute;
    font-size: 6px;
    color: var(--on-dark-muted);
  }
  .centered { left: 0; right: 0; text-align: center; }
  .content-title {
    position: absolute;
    font-size: 13px;
    font-weight: 400;
    line-height: 1.15;
    color: var(--ink);
  }
  .bullets { position: absolute; list-style: none; font-size: 9px; line-height: 12px; color: var(--ink-body); }
  .bullets li { position: relative; }
  .bullets li::before { position: absolute; }
  .lvl-1::before { content: "•"; left: -9px; }
  .lvl-2 { padding-left: 17px; } .lvl-2::before { content: "–"; left: 8px; }
  .lvl-3 { padding-left: 34px; } .lvl-3::before { content: "•"; left: 27px; font-size: 6px; }
  .lvl-4 { padding-left: 51px; } .lvl-4::before { content: "–"; left: 42px; }
  .lvl-5 { padding-left: 66px; } .lvl-5::before { content: "•"; left: 59px; font-size: 6px; }
  .bullets--small { font-size: 8px; line-height: 11.5px; }
  .footer-band {
    position: absolute; left: 0; right: 0; bottom: 0;
    height: 20px;
    background: var(--slide-dark);
  }
</style>
</head>
<body>
  <h1 class="sheet-title">Template with Dark Background_V2</h1>

  <section class="slide slide--dark" style="left:38px;top:168px;width:346px;height:259px">
    <div class="backdrop" role="img" aria-label="Decorative brand pattern in dark grey tones"></div>
    <div class="brand brand--large" style="left:116px;top:46px">Tarnel Ventures</div>
    <p class="slide__heading" style="left:116px;top:146px">Presentation Template</p>
    <p class="slide__date" style="left:143px;top:166px">November 12, 2013</p>
  </section>

  <section class="slide slide--dark" style="left:414px;top:168px;width:345px;height:259px">
    <div class="backdrop" role="img" aria-label="Decorative brand pattern in dark grey tones"></div>
    <div class="brand brand--medium" style="left:213px;top:89px">Tarnel Ventures</div>
    <p class="slide__heading" style="left:14px;top:152px">Divider</p>
  </section>

  <section class="slide slide--light" style="left:784px;top:168px;width:345px;height:259px">
    <h2 class="content-title" style="left:21px;top:32px">Title and Bulleted Content</h2>
    <ul class="bullets" style="left:29px;top:55px">
      <li class="lvl-1">Click to edit Master text styles</li>
      <li class="lvl-2">Second level</li>
      <li class="lvl-3">Third level</li>
      <li class="lvl-4">Fourth level</li>
      <li class="lvl-5">Fifth level</li>
    </ul>
    <div class="footer-band">
      <div class="brand brand--tiny" style="right:6px;top:10px">Tarnel Ventures</div>
    </div>
  </section>

  <section class="slide slide--light" style="left:38px;top:455px;width:348px;height:261px">
    <h2 class="content-title" style="left:186px;top:25px;width:158px;font-size:12px">Title and Bulleted Content on the Right</h2>
    <ul class="bullets bullets--small" style="left:195px;top:62px">
      <li class="lvl-1">Click to edit Master text styles</li>
      <li class="lvl-2">Second level</li>
      <li class="lvl-3">Third level</li>
      <li class="lvl-4">Fourth level</li>
      <li class="lvl-5">Fifth level</li>
    </ul>
    <div class="footer-band">
      <div class="brand brand--tiny" style="right:6px;top:10px">Tarnel Ventures</div>
    </div>
  </section>

  <section class="slide slide--dark" style="left:414px;top:457px;width:345px;height:259px">
    <div class="backdrop" role="img" aria-label="Decorative brand pattern in dark grey tones"></div>
    <div class="brand brand--large" style="left:116px;top:46px">Tarnel Ventures</div>
    <p class="slide__heading centered" style="top:146px">Thank You</p>
    <p class="slide__date centered" style="top:166px">November 12, 2013</p>
  </section>
</body>
</html>
```